VORELLA MILK

The packaging is to package milk. The product will be on the shelf of supermarkets. the visual identity should reflect a global product. to milk the color red must prevail. the logo, preferably should be vertically. In packaging the logo should be easy reading. know that it is prohibited to place the flag of a country on the packaging. however, we suggest that you create small symbols that can remember the flag of italy, switzerland, germany and the united states. In the attached technical drawing of Quarno Box. The logo. A photo 3 dimensions of the package. Good luck

1 - statement of the parties : the design of the packaging has 15 parties. Let us enumerate every piece of 1 to 15. where 6 is the black arrows is part number 1 (DATA DE FABRICAÇÃO/LOTE/ VÁLIDO ATÉ:) . which is in Portuguese " LEVANTE RASGUE OU CORTE " is the part number 2 . going in that direction is the number 3 , 4 , 5 . Below we part 6 (which is one half of the main panel 8 ) 7 , the part 8 is the main panel . and so on until part 15 .
2 - indication measurements : Part 1 ( 47mm width x 38mm height) , Part 2 ( 62mm width x 38mm height) , Part 3 ( 94mm width x 38mm height) , part 4 ( 62mm width x 38mm height) , Part 5 ( 47mm width x 38mm height) , Part 6 ( 47mm width x 167mm height) , Part 7 ( 62mm width x 167mm height) , part 8 ( 94mm width x 167mm height) , part 9 ( 62mm width x 167mm height) , part 10 ( 47mm 167mm width X height) , part 11 ( 47mm width x 38mm height) , part 12 ( 62mm width x 38mm height) , part 13 ( 94mm width x 38mm height) , part 14 ( 62mm width x 38mm height) , part 15 ( 47mm 38mm width X height) 3.Part 8: these are the words in Portuguese: 
part 8
The logo must be 12mmx65mm
3 This words with 10mm height X 50mm width: LEITE UHT INTEGRAL.

This box with 11mm height X 65mm width at the bottom of the main panel near 1L. "AVISO IMPORTANTE: ESTE PRODUTO NÃO DEVE SER USADO PARA ALIMENTAR CRIANÇAS MENORES DE 1(UM) ANO DE IDADE, A NÃO SER POR INDICAÇÃO EXPRESSA DE MÉDICO OU NUTRICIONISTA. O ALEITAMENTO MATERNO EVITA INFECÇÕES E ALERGIAS E DEVE SER MANTIDO ATÉ A CRIANÇA COMPLETAR 2(DOIS) ANOS DE IDADE"

part 7

INFORMAÇÃO NUTRICIONAL

Porção de 200ml (1 copo)

Quantidade por porção   %VD (*)

Valor energético  118cal=496KJ   6

Carboidratos            10g               3

Proteinas                   6,2g             8

Gorduras totais          6,0g            11

Gorduras saturadas    3,7g           17

Gorduras trans             0           VD não estabelecido

Fibra alimentar            0                0

Sódio                        143mg         6

Cálcio                        240mg       24

*% Valores Diários com base em uma dieta de 2.000 Kcal ou 8.400KJ.

Seus valores diários podem ser maiores ou menores dependendo de suas necessidades energéticas.

************************

NÃO CONTÉM GLÚTEN

***************************

NÃO NECESSITA DE REFRIGERAÇÃO.

APÓS ABERTO, CONSERVAR EM

GELADEIRA (1 A 10°C) POR ATÉ 3 DIAS.

Ingredientes: leite integral, estabilizantes citrato de sodio, difosfato de sodio, trifosfato de sodio.

part 9

O Leite integral Vorella é ultrapasteurizado

por tratamento térmico especial -UHT(Ultra 

High Temperatura), aquecido a 135 °C/145°C

por um período de 2 a 4 segundos e resfriado

rapidamente. É envasado nesta embalagem asséptica,

impermeável ao ar, à luz e aos germes. Este processo

garante um leite sem bactérias, conservando o seu 

sabor e propriedades nutritivas. 

*********************************************************

PRODUZIDO POR:

BelTOSK do Brasil LTDA

Usina de Beneficiamento

Rua Campo Alegre dos Ventos 42

CEP 47.310-000, Frutal-MG

CNPJ 61.847.290/0004-13

Registro no Ministério  da

Agricultura SIF/DIPOA sob 

o n° 0031/5627

           DISTRIBUÍDO POR:

BelTOSK do Brasil LTDA.

         INDUSTRIA BRASILEIRA

 *********************************        

CONSELHO DE LAVOURA

BRASIL

INSPECIONADO

5627

S.I.F.

```html
<!DOCTYPE html>
<html lang="pt-BR">
<head>
<meta charset="utf-8">
<title>Vorella Milk – Embalagem 1 L</title>
<link rel="stylesheet" href="https://fonts.googleapis.com/css2?family=Arimo:wght@400;700&display=swap">
<style>
:root{
  --red:#d7142a;
  --blue:#1f78c8;
  --blue-deep:#1b5aa6;
  --row-tint:#dbe9f7;
  --paper:#ffffff;
  --stage:#ececec;
  --ink:#2a2a2a;
}
*{margin:0;padding:0;box-sizing:border-box}
html,body{width:1200px;height:1200px;overflow:hidden;background:var(--stage);font-family:"Arimo",Arial,sans-serif}
.dieline{position:absolute;left:0;top:205px;width:1200px;height:789px}
.cap-row{position:absolute;left:0;top:0;width:1200px;height:146px;background:var(--paper)}
.cap-row svg{display:block}
.panel{position:absolute;top:146px;height:643px;overflow:hidden;background:var(--paper);border-left:1px solid #d9d9d9}
.p6{left:0;width:181px}
.p7{left:181px;width:238px}
.p8{left:419px;width:362px}
.p9{left:781px;width:238px}
.p10{left:1019px;width:181px}

/* front art */
.front-art{position:absolute;top:0;width:362px;height:643px}
.p6 .front-art{left:-181px}
.p8 .front-art,.p10 .front-art{left:0}
.front-art svg{position:absolute;left:0;top:0}
.product-name{position:absolute;right:18px;top:548px;color:#fff;font-size:22px}
.warning{position:absolute;left:62px;right:14px;top:578px;color:#fff;font-size:6.2px;line-height:1.3;text-transform:uppercase;text-align:justify}
.drop{position:absolute;left:18px;top:586px}
.volume{position:absolute;left:0;right:0;bottom:6px;text-align:center;color:#fff;font-weight:700;font-size:14px}

/* nutrition side */
.nutrition{position:absolute;left:10px;top:115px;width:216px;font-size:8.3px;color:var(--blue-deep)}
.nutrition table{width:100%;border-collapse:collapse;border:1.5px solid var(--blue)}
.nutrition caption{background:var(--blue);color:#fff;text-align:left;padding:4px 5px 1px;font-weight:700;font-size:12px}
.nutrition .portion{background:var(--blue);color:#fff;text-align:left;padding:0 5px 4px;font-size:8px}
.nutrition td,.nutrition th{border:1px solid var(--blue);padding:2px 4px;text-align:center;font-weight:400}
.nutrition th{text-align:left;font-weight:700}
.nutrition td:first-child{text-align:left;font-weight:700}
.nutrition tbody tr:nth-child(odd){background:var(--row-tint)}
.note{margin-top:10px;font-weight:700}
.body-text{margin-top:6px;color:var(--blue);line-height:1.35}
.strong{font-weight:700;color:var(--blue-deep)}
.flag-row{position:absolute;left:0;right:0;display:flex;justify-content:center;gap:8px}
.p7 .flag-row{top:584px}
.p9 .flag-row{top:228px}
.bottom-band{position:absolute;left:0;right:0;bottom:0;height:36px;background:var(--red)}

/* info side */
.info-logo{position:absolute;right:18px;top:70px;text-align:center;color:var(--blue)}
.info-logo .dot{width:22px;height:22px;border-radius:50%;background:var(--blue);margin:0 auto 4px}
.info-logo .name{font-size:17px}
.process{position:absolute;left:14px;right:14px;top:128px;font-size:8.4px;line-height:1.35;color:var(--blue)}
.info-red{position:absolute;left:0;right:0;top:282px;bottom:0;background:var(--red);color:#fff;padding:14px 14px 0;font-size:7.6px;line-height:1.3}
.info-red h3{font-size:10px;font-weight:700}
.info-red p{margin-bottom:8px}
.sif-box{position:absolute;left:72px;top:222px;width:92px;height:48px;background:#fff}
.info-red .volume{bottom:6px}
</style>
</head>
<body>
<main class="dieline">

  <div class="cap-row" aria-hidden="true">
    <svg width="1200" height="146" viewBox="0 0 1200 146">
      <line x1="0" y1="145.5" x2="1200" y2="145.5" stroke="#d9d9d9"/>
      <polygon points="240,0 419,0 419,146 300,146 260,70 240,30" fill="#1f78c8"/>
      <polygon points="260,70 300,146 240,146 240,30" fill="#15599e"/>
      <polygon points="840,0 1019,0 1019,40 960,130 900,40" fill="#1f78c8"/>
      <polygon points="900,40 960,130 840,70 840,0" fill="#15599e"/>
    </svg>
  </div>

  <!-- part 6 -->
  <section class="panel p6">
    <div class="front-art">
      <svg width="362" height="643" viewBox="0 0 362 643">
        <polygon points="0,330 362,180 362,643 0,643" fill="#d7142a"/>
        <circle cx="181" cy="72" r="30" fill="#1f78c8"/>
        <text x="181" y="152" text-anchor="middle" font-family="Arimo, sans-serif" font-size="58" fill="#1f78c8">vorella</text>
        <text transform="translate(22,560) rotate(-26)" font-family="Arimo, sans-serif" font-weight="700" font-size="190" fill="#ffffff">milk</text>
      </svg>
      <p class="product-name">Leite UHT Integral</p>
      <p class="warning">Aviso importante: este produto não deve ser usado para alimentar crianças menores de 1(um) ano de idade, a não ser por indicação expressa de médico ou nutricionista. O aleitamento materno evita infecções e alergias e deve ser mantido até a criança completar 2(dois) anos de idade</p>
      <svg class="drop" width="14" height="20" viewBox="0 0 14 20"><path d="M7 0C7 0 0 9 0 13a7 7 0 0 0 14 0C14 9 7 0 7 0z" fill="#fff"/></svg>
      <p class="volume">1 L</p>
    </div>
  </section>

  <!-- part 7 -->
  <section class="panel p7">
    <div class="nutrition">
      <table>
        <caption>INFORMAÇÃO NUTRICIONAL</caption>
        <thead>
          <tr><td class="portion" colspan="3" style="border:none;font-weight:400">Porção de 200ml (1 copo)</td></tr>
          <tr><th>Quantidade por porção</th><th></th><th style="text-align:center">%VD (*)</th></tr>
        </thead>
        <tbody>
          <tr><td>Valor energético</td><td>118 cal = 496 KJ</td><td>6</td></tr>
          <tr><td>Carboidratos</td><td>10g</td><td>3</td></tr>
          <tr><td>Proteínas</td><td>6,2g</td><td>8</td></tr>
          <tr><td>Gorduras totais</td><td>6,0g</td><td>11</td></tr>
          <tr><td>Gorduras saturadas</td><td>3,7g</td><td>17</td></tr>
          <tr><td>Gorduras trans</td><td>0</td><td>VD não</td></tr>
          <tr><td>Fibra alimentar</td><td>0</td><td>0</td></tr>
          <tr><td>Sódio</td><td>143g</td><td>6</td></tr>
          <tr><td>Cálcio</td><td>240mg</td><td>24</td></tr>
        </tbody>
      </table>
      <p class="note">(*) % Valores Diários com base em uma dieta de 2.000 Kcal ou 8.400KJ.</p>
      <p class="body-text">Seus valores diários podem ser maiores ou menores dependendo de suas necessidades energéticas.</p>
      <p class="body-text strong">NÃO CONTÉM GLÚTEN</p>
      <p class="body-text">NÃO NECESSITA DE REFRIGERAÇÃO.<br>APÓS ABERTO, CONSERVAR EM<br>GELADEIRA (1 A 10°C) POR ATÉ 3 DIAS.</p>
      <p class="body-text"><span class="strong">Ingredientes:</span> leite integral, estabilizantes citrato de sodio, difosfato de sodio, trifosfato de sodio.</p>
    </div>
    <div class="flag-row">
      <svg width="18" height="18" viewBox="0 0 18 18" role="img" aria-label="Itália"><clipPath id="c1"><circle cx="9" cy="9" r="9"/></clipPath><g clip-path="url(#c1)"><rect width="6" height="18" fill="#1a9b47"/><rect x="6" width="6" height="18" fill="#fff"/><rect x="12" width="6" height="18" fill="#d7142a"/></g><circle cx="9" cy="9" r="8.5" fill="none" stroke="#bbb"/></svg>
      <svg width="18" height="18" viewBox="0 0 18 18" role="img" aria-label="Suíça"><circle cx="9" cy="9" r="9" fill="#d7142a"/><rect x="7.5" y="4" width="3" height="10" fill="#fff"/><rect x="4" y="7.5" width="10" height="3" fill="#fff"/></svg>
      <svg width="18" height="18" viewBox="0 0 18 18" role="img" aria-label="Alemanha"><clipPath id="c2"><circle cx="9" cy="9" r="9"/></clipPath><g clip-path="url(#c2)"><rect width="18" height="6" fill="#111"/><rect y="6" width="18" height="6" fill="#d7142a"/><rect y="12" width="18" height="6" fill="#f2c300"/></g></svg>
      <svg width="18" height="18" viewBox="0 0 18 18" role="img" aria-label="Estados Unidos"><clipPath id="c3"><circle cx="9" cy="9" r="9"/></clipPath><g clip-path="url(#c3)"><rect width="18" height="18" fill="#fff"/><rect width="18" height="3" fill="#d7142a"/><rect y="6" width="18" height="3" fill="#d7142a"/><rect y="12" width="18" height="3" fill="#d7142a"/><rect width="9" height="9" fill="#1b3f8f"/></g><circle cx="9" cy="9" r="8.5" fill="none" stroke="#bbb"/></svg>
    </div>
    <div class="bottom-band"><p class="volume">1 L</p></div>
  </section>

  <!-- part 8 -->
  <section class="panel p8">
    <div class="front-art">
      <svg width="362" height="643" viewBox="0 0 362 643">
        <polygon points="0,330 362,180 362,643 0,643" fill="#d7142a"/>
        <circle cx="181" cy="72" r="30" fill="#1f78c8"/>
        <text x="181" y="152" text-anchor="middle" font-family="Arimo, sans-serif" font-size="58" fill="#1f78c8">vorella</text>
        <text transform="translate(22,560) rotate(-26)" font-family="Arimo, sans-serif" font-weight="700" font-size="190" fill="#ffffff">milk</text>
      </svg>
      <p class="product-name">Leite UHT Integral</p>
      <p class="warning">Aviso importante: este produto não deve ser usado para alimentar crianças menores de 1(um) ano de idade, a não ser por indicação expressa de médico ou nutricionista. O aleitamento materno evita infecções e alergias e deve ser mantido até a criança completar 2(dois) anos de idade</p>
      <svg class="drop" width="14" height="20" viewBox="0 0 14 20"><path d="M7 0C7 0 0 9 0 13a7 7 0 0 0 14 0C14 9 7 0 7 0z" fill="#fff"/></svg>
      <p class="volume">1 L</p>
    </div>
  </section>

  <!-- part 9 -->
  <section class="panel p9">
    <div class="info-logo"><div class="dot"></div><p class="name">vorella</p></div>
    <p class="process"><strong>Leite integral Vorella</strong> é ultrapasteurizado por tratamento térmico especial -UHT(Ultra High Temperatura), aquecido a 135 °C/145°C por um período de 2 a 4 segundos e resfriado rapidamente. É envasado nesta embalagem asséptica, impermeável ao ar, à luz e aos germes. Este processo garante um leite sem bactérias, conservando o seu sabor e propriedades nutritivas.</p>
    <div class="flag-row">
      <svg width="18" height="18" viewBox="0 0 18 18" role="img" aria-label="Itália"><clipPath id="d1"><circle cx="9" cy="9" r="9"/></clipPath><g clip-path="url(#d1)"><rect width="6" height="18" fill="#1a9b47"/><rect x="6" width="6" height="18" fill="#fff"/><rect x="12" width="6" height="18" fill="#d7142a"/></g><circle cx="9" cy="9" r="8.5" fill="none" stroke="#bbb"/></svg>
      <svg width="18" height="18" viewBox="0 0 18 18" role="img" aria-label="Suíça"><circle cx="9" cy="9" r="9" fill="#d7142a"/><rect x="7.5" y="4" width="3" height="10" fill="#fff"/><rect x="4" y="7.5" width="10" height="3" fill="#fff"/></svg>
      <svg width="18" height="18" viewBox="0 0 18 18" role="img" aria-label="Alemanha"><clipPath id="d2"><circle cx="9" cy="9" r="9"/></clipPath><g clip-path="url(#d2)"><rect width="18" height="6" fill="#111"/><rect y="6" width="18" height="6" fill="#d7142a"/><rect y="12" width="18" height="6" fill="#f2c300"/></g></svg>
      <svg width="18" height="18" viewBox="0 0 18 18" role="img" aria-label="Estados Unidos"><clipPath id="d3"><circle cx="9" cy="9" r="9"/></clipPath><g clip-path="url(#d3)"><rect width="18" height="18" fill="#fff"/><rect width="18" height="3" fill="#d7142a"/><rect y="6" width="18" height="3" fill="#d7142a"/><rect y="12" width="18" height="3" fill="#d7142a"/><rect width="9" height="9" fill="#1b3f8f"/></g><circle cx="9" cy="9" r="8.5" fill="none" stroke="#bbb"/></svg>
    </div>
    <div class="info-red">
      <h3>PRODUZIDO POR:</h3>
      <p>BelTOSK do Brasil LTDA<br>Usina de Beneficiamento<br>Rua Campo Alegre dos Ventos 42<br>CEP 47.310-000, Frutal-MG<br>CNPJ 61.847.290/0004-13<br>Registro no Ministério da<br>Agricultura SIF/DIPOA sob<br>o n° 0031/5627</p>
      <h3>DISTRIBUÍDO POR:</h3>
      <p>BelTOSK do Brasil LTDA.<br>INDUSTRIA BRASILEIRA</p>
      <p>CONSELHO DE LAVOURA<br>BRASIL<br>INSPECIONADO<br>5627<br>S.I.F.</p>
      <div class="sif-box"></div>
      <p class="volume">1 L</p>
    </div>
  </section>

  <!-- part 10 -->
  <section class="panel p10">
    <div class="front-art">
      <svg width="362" height="643" viewBox="0 0 362 643">
        <polygon points="0,330 362,180 362,643 0,643" fill="#d7142a"/>
        <circle cx="181" cy="72" r="30" fill="#1f78c8"/>
        <text x="181" y="152" text-anchor="middle" font-family="Arimo, sans-serif" font-size="58" fill="#1f78c8">vorella</text>
        <text transform="translate(22,560) rotate(-26)" font-family="Arimo, sans-serif" font-weight="700" font-size="190" fill="#ffffff">milk</text>
      </svg>
      <p class="product-name">Leite UHT Integral</p>
      <p class="warning">Aviso importante: este produto não deve ser usado para alimentar crianças menores de 1(um) ano de idade, a não ser por indicação expressa de médico ou nutricionista. O aleitamento materno evita infecções e alergias e deve ser mantido até a criança completar 2(dois) anos de idade</p>
      <svg class="drop" width="14" height="20" viewBox="0 0 14 20"><path d="M7 0C7 0 0 9 0 13a7 7 0 0 0 14 0C14 9 7 0 7 0z" fill="#fff"/></svg>
      <p class="volume">1 L</p>
    </div>
  </section>

</main>
</body>
</html>
```